Company Stationary

I'd like a template to use for company stationery. We frequently write short 1 - 2 page Word documents (which we save as PDF) to clients and prospects and the presentation is boring and doesn't look professional. I am looking for a Word template that will convey a better sense of professionalism. The design should include our logo (attached) but be simple and elegant. It should save nicely as a PDF, since that is how we will send the files via email.

Target Market(s)

Financial Institutions

Industry/Entity Type

Financial Service

Font styles to use
Serif

Colors

Designer to choose colors to be used in the design.

Requirements
Must have
• Simple design. Needs to be subtle. I don't want the design to be more interesting than the message we are writing.
Nice to have
• When the reader sees it, I want them to feel they are reading something published by a large, very successful company.
Should not have
• Not overpowering design and colors.

```html
<!DOCTYPE html>
<html lang="en">
<head>
<meta charset="utf-8">
<title>Calderline Letterhead</title>
<link href="https://fonts.googleapis.com/css2?family=Lato:wght@400;700;900&display=swap" rel="stylesheet">
<style>
  :root {
    --backdrop: #ececec;
    --paper: #ffffff;
    --ink: #111111;
    --muted: #222222;
    --accent: #ee1c12;
    --signature-tone: #e4e4e4;
  }
  html, body {
    margin: 0;
    padding: 0;
    width: 1200px;
    height: 815px;
    overflow: hidden;
    background: var(--backdrop);
    font-family: "Lato", Arial, sans-serif;
  }
  .canvas {
    position: relative;
    width: 1200px;
    height: 815px;
  }
  .sheet {
    position: absolute;
    width: 490px;
    height: 692px;
    background: var(--paper);
    border-top: 3px solid var(--ink);
    box-sizing: border-box;
  }
  .sheet--letter { left: 80px; top: 64px; }
  .sheet--blank { left: 636px; top: 69px; }

  .brand {
    position: absolute;
    left: 32px;
    top: 36px;
    font-weight: 900;
    font-size: 24px;
    letter-spacing: 0.3px;
    color: var(--ink);
    line-height: 1;
    display: flex;
    align-items: center;
    gap: 7px;
  }
  .brand__dot {
    width: 9px;
    height: 9px;
    background: var(--accent);
    border-radius: 50%;
  }

  .contact {
    position: absolute;
    left: 364px;
    top: 32px;
    height: 56px;
    border-left: 1px solid var(--ink);
    padding-left: 10px;
    font-size: 7.2px;
    line-height: 9px;
    color: var(--muted);
  }
  .contact__address { margin-bottom: 3px; }
  .contact__row { display: flex; align-items: center; gap: 6px; }
  .contact__row svg { width: 6px; height: 6px; fill: var(--accent); }

  .letter-body {
    position: absolute;
    left: 32px;
    top: 204px;
    width: 360px;
    font-size: 7.6px;
    line-height: 11.6px;
    color: var(--ink);
  }
  .letter-body p { margin: 0 0 11.4px 0; }

  .signature {
    position: absolute;
    left: 36px;
    top: 480px;
    width: 140px;
    height: 24px;
    background: var(--signature-tone);
  }

  .footer {
    position: absolute;
    left: 0;
    bottom: 0;
    width: 490px;
    height: 21px;
  }
  .footer svg { display: block; width: 490px; height: 21px; }
  .footer__url {
    position: absolute;
    right: 33px;
    top: 5px;
    font-size: 7.6px;
    color: var(--paper);
    letter-spacing: 0.2px;
  }
</style>
</head>
<body>
<div class="canvas">

  <section class="sheet sheet--letter">
    <div class="brand"><span class="brand__name">Calderline</span><span class="brand__dot"></span></div>

    <address class="contact" style="font-style:normal">
      <div class="contact__address">Calderline, LLC<br>218 Harbor Lane<br>Fairhaven, NJ 07110</div>
      <div class="contact__row"><svg viewBox="0 0 10 10"><path d="M2 0 L4 0 L4.5 3 L3 4 C4 6 5 7 6.5 7.5 L7.5 6 L10 6.5 L10 9 C10 9.6 9.6 10 9 10 C4 10 0 6 0 1 C0 0.4 0.4 0 1 0 Z"/></svg>(555) 310-4827</div>
      <div class="contact__row"><svg viewBox="0 0 10 10"><rect x="2" y="0" width="6" height="3"/><rect x="0" y="3.5" width="10" height="4"/><rect x="2" y="7" width="6" height="3"/></svg>(555) 310-4800</div>
      <div class="contact__row"><svg viewBox="0 0 10 10"><path d="M0 1.5 L10 1.5 L10 8.5 L0 8.5 Z M0.6 2 L5 5.5 L9.4 2"/></svg>hello@calderline.com</div>
    </address>

    <div class="letter-body">
      <p>Lorem ipsum dolor sit amet, consectetur adipiscing elit. Praesent non est diam. Vivamus risus sem, gravida sit amet nibh ut, ornare lobortis ante. Aliquam sollicitudin, mauris tincidunt semper venenatis, orci est pretium augue, ut vestibulum felis velit bibendum urna. Integer sollicitudin aliquet ligula, non ultricies nisl efficitur nec. Aliquam felis lorem, facilisis ac condimentum quis, consectetur volutpat lacus. Proin fermentum sem quis elit efficitur, eu tempus magna maximus.</p>
      <p>&nbsp;Aenean a mi tortor. Morbi pretium mi sed cursus vehicula. Lorem ipsum dolor sit amet, consectetur adipiscing elit. In finibus eros ac maximus finibus. Nunc pretium pellentesque tellus. Nullam accumsan nisl non diam commodo sagittis. Nunc et ante sit amet urna auctor convallis. Maecenas sed fringilla metus, sit amet vulputate felis. Morbi eget tempor nisi. Aliquam erat volutpat. Aenean laoreet interdum tempus.</p>
      <p>&nbsp;Maecenas dignissim placerat mauris, vitae sollicitudin ex. Integer bibendum maximus mauris, ac tempor urna viverra id. Integer tincidunt lobortis nisl at posuere. Sed faucibus vulputate finibus. Maecenas convallis, sem quis pellentesque cursus, urna quam aliquam augue, quis porttitor eros est nec lectus. Sed mattis at tellus ut blandit. Aenean nunc magna, viverra sed mauris vel, porta finibus lacus. Nullam bibendum turpis rutrum porta placerat</p>
      <p>Aenean a mi tortor. Morbi pretium mi sed cursus vehicula. Lorem ipsum dolor sit amet, consectetur adipiscing elit. In finibus eros ac maximus finibus. Nunc pretium pellentesque tellus. Nullam accumsan nisl non diam commodo sagittis. Nunc et ante sit amet urna auctor convallis. Maecenas sed fringilla metus, sit amet vulputate felis. Morbi eget tempor nisi. Aliquam erat volutpat. Aenean laoreet interdum tempus. .</p>
    </div>

    <div class="signature" role="img" aria-label="Handwritten signature of the sender"></div>

    <footer class="footer">
      <svg viewBox="0 0 490 21" preserveAspectRatio="none">
        <rect x="0" y="11" width="336" height="10" fill="var(--accent)"/>
        <path d="M338 21 C346 21 348 1 362 1 L490 1 L490 21 Z" fill="var(--ink)"/>
      </svg>
      <span class="footer__url">www.calderline.com</span>
    </footer>
  </section>

  <section class="sheet sheet--blank">
    <div class="brand"><span class="brand__name">Calderline</span><span class="brand__dot"></span></div>

    <footer class="footer">
      <svg viewBox="0 0 490 21" preserveAspectRatio="none">
        <rect x="0" y="11" width="336" height="10" fill="var(--accent)"/>
        <path d="M338 21 C346 21 348 1 362 1 L490 1 L490 21 Z" fill="var(--ink)"/>
      </svg>
      <span class="footer__url">www.calderline.com</span>
    </footer>
  </section>

</div>
</body>
</html>
```